Are you a woman over 50 who can’t lose weight?

Ads attracting 50 and older women/men who are looking for holistic metabolism improving solutions and can’t lose weight on their own.(please see my website: gobrivanhealth.com) Descriptions saying this is a program designed to improve your metabolism NOT another fad diet. Every plan is customized to each patients needs (no cookie cutter plans) and overseen by a healthcare provider. Will be taught which foods are best for their individual body with special technology. No exercise needed to lose weight or inches. Dr. Neil Sorrow, DC who will oversee your care was listed as the 2018 Wellness Champion for all of Central Louisiana. Our patients lose up to one pound of fat per day AND are supported on keeping it off. We do Body Composition analyses, 3-D body scans, Biocommunication, and Body Fat elimination technologies to help you succeed. We have been serving Mivo for 12 years and have great reviews online. We are an A+ business with the Fair Trade Registry. We are locally owned and not affiliated with any franchises.

Target Market(s)

Women 50-70years old

Industry/Entity Type

Health And Wellness

Font styles to use
Serif

Colors

Designer to choose colors to be used in the design.

Requirements
Must have
• Brivan logo, website to see testimonials, 3-D Body scan for first time visitor for $20 ($150 value). Scan will show measurements, body fat percentage, and lots of other metabolic information.
Nice to have
• Look at my website: gobrivanhealth.com for my logo please and other information

```html
<!DOCTYPE html>
<html lang="en">
<head>
<meta charset="utf-8">
<title>Brivan – Lifelong Weight Loss Flyer</title>
<link rel="stylesheet" href="https://fonts.googleapis.com/css2?family=Bebas+Neue&family=Josefin+Sans:wght@300;400&family=Raleway:wght@400;500;600;700&display=swap">
<style>
  :root {
    --backdrop: #8a8a8a;
    --green: #80bc41;
    --charcoal: #464646;
    --ink: #3a3a3a;
    --white: #ffffff;
    --body-grey: #555555;
  }
  * { box-sizing: border-box; margin: 0; padding: 0; }
  html, body { width: 1200px; height: 1200px; overflow: hidden; background: var(--backdrop); }
  .flyer {
    position: absolute; left: 217px; top: 63px;
    width: 766px; height: 1074px; background: var(--white); overflow: hidden;
    font-family: "Raleway", sans-serif;
  }
  .flyer-art { position: absolute; left: 0; top: 0; width: 766px; height: 1074px; }
  .abs { position: absolute; }

  .headline {
    left: 64px; top: 32px; font-family: "Bebas Neue", sans-serif;
    font-size: 54px; line-height: 47px; color: var(--green);
  }
  .headline .lead { color: var(--ink); }

  .brand { left: 580px; top: 30px; width: 160px; text-align: center; }
  .brand-name {
    font-family: "Raleway", sans-serif; font-weight: 700; font-size: 38px;
    color: var(--ink); line-height: 1; letter-spacing: -0.5px;
  }
  .brand-tag {
    font-weight: 700; font-size: 7.5px; letter-spacing: 0.8px; color: var(--green);
    margin-top: 6px;
  }

  .tagline {
    left: 64px; top: 346px; font-family: "Josefin Sans", sans-serif;
    font-size: 27px; line-height: 36px; color: var(--white);
  }

  .intro {
    left: 0; top: 508px; width: 766px; text-align: center;
    font-size: 11.5px; line-height: 16.5px; color: var(--body-grey);
  }

  .offer-panel-text { left: 278px; top: 590px; color: var(--white); }
  .offer-title { font-weight: 700; font-size: 14px; line-height: 18px; width: 330px; }
  .benefits { list-style: none; margin-top: 7px; }
  .benefits li {
    position: relative; padding-left: 31px; font-weight: 500;
    font-size: 14px; line-height: 22.5px;
  }
  .benefits svg { position: absolute; left: 5px; top: 4px; }

  .scan-offer {
    left: 56px; top: 561px; width: 204px; height: 204px; text-align: center;
    font-family: "Josefin Sans", sans-serif; color: var(--ink);
    display: flex; flex-direction: column; align-items: center; justify-content: center;
  }
  .scan-title { font-weight: 300; font-size: 21px; line-height: 28px; }
  .scan-price { font-weight: 300; font-size: 12.5px; margin-top: 4px; }
  .scan-price strong { font-weight: 400; font-size: 22px; }
  .scan-note {
    font-weight: 300; font-size: 8.5px; line-height: 11px; color: var(--green);
    margin-top: 14px; letter-spacing: 0.3px;
  }

  .steps-title {
    left: 64px; top: 852px; font-family: "Josefin Sans", sans-serif;
    font-size: 22px; letter-spacing: 1px; color: var(--green);
  }
  .steps-copy {
    left: 64px; top: 883px; width: 640px; color: var(--white);
    font-size: 12px; line-height: 17.5px;
  }
  .steps-copy p + p { margin-top: 17px; }

  .info-pill {
    left: 68px; top: 1006px; width: 396px; height: 31px; border-radius: 16px;
    overflow: hidden; display: flex; font-size: 14px; letter-spacing: 1.2px;
  }
  .info-pill .label { width: 185px; background: var(--white); color: var(--ink); padding: 7px 0 0 20px; }
  .info-pill .url { flex: 1; background: var(--green); color: var(--white); padding: 7px 0 0 10px; }

  .contact {
    left: 565px; top: 965px; color: var(--white); font-weight: 700;
    font-size: 15.5px; line-height: 21px;
  }
</style>
</head>
<body>
<main class="flyer">
  <svg class="flyer-art" viewBox="0 0 766 1074" aria-hidden="false">
    <defs>
      <linearGradient id="photoTone" x1="0" y1="0" x2="1" y2="1">
        <stop offset="0" stop-color="#eef2f4"/>
        <stop offset="0.45" stop-color="#dfe4e0"/>
        <stop offset="1" stop-color="#6e7480"/>
      </linearGradient>
      <linearGradient id="meadow" x1="0" y1="0" x2="0" y2="1">
        <stop offset="0" stop-color="#b9c3a8" stop-opacity="0"/>
        <stop offset="1" stop-color="#6f8a4e"/>
      </linearGradient>
    </defs>
    <g role="img" aria-label="Photo: smiling older couple standing outdoors in a green hillside landscape">
      <rect class="hero-photo" x="0" y="0" width="766" height="520" fill="url(#photoTone)"/>
      <rect x="0" y="300" width="400" height="220" fill="url(#meadow)"/>
    </g>
    <path class="band-dark" d="M0,485 C230,425 520,455 766,398 L766,520 L0,520 Z" fill="var(--charcoal)"/>
    <path class="band-green" d="M0,500 C250,455 520,472 766,438 L766,520 L0,520 Z" fill="var(--green)"/>
    <path class="band-white" d="M0,508 C250,478 520,495 766,470 L766,520 L0,520 Z" fill="var(--white)"/>
    <rect x="0" y="519" width="766" height="200" fill="var(--white)"/>

    <path class="offer-panel" d="M217,578 L596,578 Q614,578 606,596 L543,738 Q536,753 518,753 L217,753 Z" fill="var(--green)"/>

    <path class="band-dark" d="M0,705 C160,770 320,800 470,800 C610,800 690,790 766,808 L766,1074 L0,1074 Z" fill="var(--charcoal)"/>
    <path class="band-green" d="M0,742 C170,790 370,815 766,806 L766,1074 L0,1074 Z" fill="var(--green)"/>
    <path class="band-white" d="M0,784 C200,818 430,828 766,816 L766,1074 L0,1074 Z" fill="var(--white)"/>
    <path class="band-dark" d="M0,790 C200,826 430,836 766,822 L766,1074 L0,1074 Z" fill="var(--charcoal)"/>

    <circle class="scan-badge" cx="158" cy="663" r="101" fill="var(--white)" stroke="var(--green)" stroke-width="4"/>
  </svg>

  <h1 class="abs headline"><span class="lead">Are you over 50?</span><br>Do you want<br>lifelong<br>weight loss?</h1>

  <div class="abs brand">
    <div class="brand-name">Brivan</div>
    <div class="brand-tag">WEIGHT LOSS &amp; BODY BALANCING</div>
  </div>

  <p class="abs tagline">Improve your metabolism<br>NOT another fad diet.</p>

  <p class="abs intro">Every plan is customized to each patients needs (no cookie cutter plans) and overseen by a healthcare provider.<br>Will be taught which foods are best for their individual body with special technology.</p>

  <div class="abs scan-offer">
    <div class="scan-title">3-D Body Scan<br>for First Time Visitor</div>
    <div class="scan-price"><strong>$20</strong> ($150 value)</div>
    <div class="scan-note">Scan will show measurements,<br>body fat percentage, and lots<br>of other metabolic information.</div>
  </div>

  <div class="abs offer-panel-text">
    <p class="offer-title">Biocommunication, and Body Fat elimination technologies to help you succeed</p>
    <ul class="benefits">
      <li><svg width="18" height="18" viewBox="0 0 18 18"><path d="M2,10 L6,16 L16,1" fill="none" stroke="#fff" stroke-width="2.2" stroke-linecap="round" stroke-linejoin="round"/></svg>No Exercise</li>
      <li><svg width="18" height="18" viewBox="0 0 18 18"><path d="M2,10 L6,16 L16,1" fill="none" stroke="#fff" stroke-width="2.2" stroke-linecap="round" stroke-linejoin="round"/></svg>No Hunger</li>
      <li><svg width="18" height="18" viewBox="0 0 18 18"><path d="M2,10 L6,16 L16,1" fill="none" stroke="#fff" stroke-width="2.2" stroke-linecap="round" stroke-linejoin="round"/></svg>No Drugs</li>
      <li><svg width="18" height="18" viewBox="0 0 18 18"><path d="M2,10 L6,16 L16,1" fill="none" stroke="#fff" stroke-width="2.2" stroke-linecap="round" stroke-linejoin="round"/></svg>3-D body scans</li>
    </ul>
  </div>

  <h2 class="abs steps-title">LOSE WEIGHT IN EASY STEP</h2>
  <div class="abs steps-copy">
    <p>Dr. Neil Sorrow, DC who will oversee your care was listed as the 2018 Wellness Champion for all of Central Louisiana. Our patients lose up to one pound of fat per day AND are supported on keeping it off.</p>
    <p>We have been serving Mivo for 12 years and have great reviews online.<br>We are an A+ business with the Fair Trade Registry.</p>
  </div>

  <div class="abs info-pill">
    <span class="label">more information</span>
    <span class="url">www.gobrivanhealth.com</span>
  </div>

  <address class="abs contact" style="font-style:normal">1450 Alder Ridge Road<br>Mivo, LA 70000<br>555-014-2278</address>
</main>
</body>
</html>
```